Letterhead design - Harwick Group

We have just had our Logo created and our now wantng a letterhead design to incorporate this. Please use the same colours as in the logo, which is attached.
Please use the company details below
P O Box 86, Bleneheim 7315
Ph: 03 642 1937
dave@harwickgroup.co.nz
We would like a professional look
We need an overall letterhead design for our varied group of buisinesses which are based in NZ and overseas. We grow and develop buisinesses. Our companies began in NZ but we now have branches overseas as well. People are our greatest asset and we employ some incredible staff. Our buisinesses are scientific, innovative and growing in size and expertise with a financial base.

Target Market(s)

Professionals

Industry/Entity Type

Investment

Requirements
Must have
• Easy to read.
• Please use the same colours as in the logo
• Please use the company details below
• P O Box 86, Bleneheim 7315
• Ph: 03 642 1937
• dave@harwickgroup.co.nz

```html
<!DOCTYPE html>
<html lang="en">
<head>
<meta charset="utf-8">
<title>Harwick Group – Letterhead</title>
<link href="https://fonts.googleapis.com/css2?family=Lato:wght@700;900&display=swap" rel="stylesheet">
<style>
  :root {
    --brand-green: #3ff23f;
    --mid-green: #3cb44a;
    --slate: #536366;
    --paper: #ffffff;
    --backdrop: #eef0f0;
  }
  html, body {
    margin: 0;
    width: 1200px;
    height: 1200px;
    overflow: hidden;
    background: var(--backdrop);
  }
  .letterhead {
    position: absolute;
    left: 144px;
    top: 30px;
    width: 802px;
    height: 1143px;
    background: var(--paper);
    font-family: "Lato", sans-serif;
    overflow: hidden;
  }
  .band {
    position: absolute;
    left: 0;
    width: 802px;
    height: 74px;
  }
  .band--top {
    top: 0;
    background: linear-gradient(180deg, var(--slate) 0%, var(--mid-green) 45%, var(--brand-green) 100%);
  }
  .band--bottom {
    bottom: 0;
    height: 80px;
    background: linear-gradient(0deg, var(--slate) 0%, var(--mid-green) 45%, var(--brand-green) 100%);
  }
  .brand {
    position: absolute;
    left: 20px;
    top: 80px;
    height: 74px;
    display: flex;
    align-items: center;
    gap: 16px;
  }
  .brand__mark {
    width: 74px;
    height: 74px;
    background: var(--brand-green);
  }
  .brand__name {
    font-weight: 900;
    font-size: 29px;
    letter-spacing: 0.5px;
    color: var(--slate);
    text-transform: uppercase;
    line-height: 1;
    white-space: nowrap;
  }
  .contact {
    position: absolute;
    left: 473px;
    top: 80px;
    height: 74px;
    padding-left: 12px;
    border-left: 2px solid var(--slate);
    display: flex;
    flex-direction: column;
    justify-content: space-between;
  }
  .contact__row {
    display: flex;
    align-items: center;
    gap: 12px;
    font-weight: 700;
    font-size: 16.5px;
    color: var(--slate);
    height: 20px;
    white-space: nowrap;
  }
  .contact__icon {
    width: 18px;
    height: 18px;
    flex: none;
  }
  .contact__email { text-transform: uppercase; }
</style>
</head>
<body>
<main class="letterhead">
  <div class="band band--top" role="img" aria-label="Green and slate header band"></div>

  <div class="brand">
    <div class="brand__mark"></div>
    <div class="brand__name">Harwick Group</div>
  </div>

  <div class="contact">
    <div class="contact__row">
      <svg class="contact__icon" viewBox="0 0 24 24" aria-hidden="true">
        <path d="M6.6 2.5 9.3 5.6 7.6 8.2c1.3 3 3.4 5.1 6.3 6.4l2.6-1.7 3.1 2.7-1.6 3.9C10.6 19.2 4.8 13.4 4.5 4.1Z" fill="var(--slate)"/>
      </svg>
      <span>03 642 1937</span>
    </div>
    <div class="contact__row">
      <svg class="contact__icon" viewBox="0 0 24 24" fill="none" stroke="var(--slate)" stroke-width="1.3" aria-hidden="true">
        <circle cx="12" cy="12" r="10"/>
        <ellipse cx="12" cy="12" rx="4.5" ry="10"/>
        <path d="M2 12h20M3.5 7h17M3.5 17h17"/>
      </svg>
      <span>P O BOX 86, BLENEHEIM 7315</span>
    </div>
    <div class="contact__row">
      <svg class="contact__icon" viewBox="0 0 24 24" fill="none" stroke="var(--slate)" stroke-width="1.5" aria-hidden="true">
        <path d="M12 22s-7-7.2-7-12.5a7 7 0 0 1 14 0C19 14.8 12 22 12 22Z"/>
        <circle cx="12" cy="9.5" r="2.6"/>
      </svg>
      <span class="contact__email">dave@harwickgroup.co.nz</span>
    </div>
  </div>

  <div class="band band--bottom" role="img" aria-label="Green and slate footer band"></div>
</main>
</body>
</html>
```